I want a business letter head designed, one that I can have printed but also one that I can use as an insert for proforma documentation that is printed in house.

Business name : RJ Pemberly & Associates
Address: PO Box 732
Coralbrook Qld 4871

Type of business: Accounting practice- accounting, taxation, audit, self managed superannuation,

Colour scheme: black and blue - previously designed a business card; however the blue that is one the cards is very washed out and I am not particularly happy with it.

```html
<!DOCTYPE html>
<html lang="en">
<head>
<meta charset="utf-8">
<title>RJ Pemberly &amp; Associates – Letterhead</title>
<link rel="stylesheet" href="https://fonts.googleapis.com/css2?family=Crimson+Text:wght@700&family=Roboto+Slab:wght@300;400&display=swap">
<style>
  :root {
    --backdrop: #e6e6e6;
    --paper: #ffffff;
    --ink: #111111;
    --brand-blue: #1ef0f7;
    --brand-blue-faint: #effeff;
    --rule: #555555;
  }
  * { margin: 0; padding: 0; box-sizing: border-box; }
  html, body {
    width: 923px; height: 1200px; overflow: hidden;
    background: var(--backdrop);
  }
  .letterhead {
    position: absolute; left: 30px; top: 52px;
    width: 862px; height: 1116px;
    background: var(--paper);
    overflow: hidden;
    box-shadow: 0 2px 8px rgba(0,0,0,0.25);
  }
  .brand-square {
    position: absolute; left: 22px; top: 31px;
    width: 81px; height: 81px;
    background: var(--brand-blue);
  }
  .brand-name {
    position: absolute; left: 123px; top: 22px;
    font-family: "Crimson Text", Georgia, serif;
    font-weight: 700; font-size: 37px; line-height: 35px;
    color: var(--ink);
    text-align: center;
  }
  .contact {
    position: absolute; left: 567px; top: 20px;
    padding-left: 11px;
    border-left: 1px solid var(--rule);
    font-family: "Roboto Slab", Georgia, serif;
    font-weight: 400; font-size: 15px; line-height: 19px;
    color: var(--ink);
  }
  .contact-line { display: flex; align-items: center; gap: 5px; }
  .contact-line svg { width: 10px; height: 10px; fill: var(--ink); }
  .postal { margin-top: 7px; }
  .decor-block {
    position: absolute; left: 0; top: 602px;
    width: 537px; height: 514px;
    background: var(--brand-blue-faint);
  }
  .services {
    position: absolute; left: 373px; top: 1045px;
    font-family: "Roboto Slab", Georgia, serif;
    font-weight: 400; font-size: 18px; line-height: 26px;
    color: var(--ink);
  }
</style>
</head>
<body>
  <main class="letterhead">
    <div class="brand-square"></div>
    <h1 class="brand-name">RJ Pemberly<br>&amp; Associates</h1>

    <address class="contact" style="font-style: normal;">
      <div class="contact-line">
        <svg viewBox="0 0 10 10" aria-hidden="true"><path d="M2 0h6v10H2z M3 1v5h4V1z"/></svg>
        <span>0400 123 987</span>
      </div>
      <div class="contact-line">
        <svg viewBox="0 0 10 10" aria-hidden="true"><path d="M0 2h10v7H0z"/></svg>
        <span>rachel@rjpemberly.com.au</span>
      </div>
      <div class="postal">PO Box 732<br>Coralbrook Qld 4871</div>
    </address>

    <div class="decor-block"></div>

    <ul class="services" style="list-style: none;">
      <li>• Accounting Practice- Accounting • Taxation • Audit</li>
      <li>• Self Managed Superannuation</li>
    </ul>
  </main>
</body>
</html>
```